Mission Vision and Values Infographic

We are a healthcare organisation and would like to create a graphic which showcases our Mission, Vision and Values in a clear and beautiful manner.

Attached is:

* Our mission vision and values.
* Style Guide
* Examples of other designs found on the web
* Logo

Your design should be Simple, Clear, Professional and Beautiful.

If you prefer, you can submit a Basic design to start off with for initial feedback before then refining in a future submission. Please check back in the comments section as I will be providing additional general remarks if needed.

The design needs to be created in a tool which will then allow us to modify it in the future…. Ideally either Adobe InDesign, Adobe Illustrator or Adobe Photoshop. Vector is preferred.

All together, the whole design needs to be:

* Printable on one sheet of A3 size paper (to go on our wall)
* Be able to go on a webpage

So there might be slight variations for bigger and smaller displays. For example, the A3 Page will have all three - Mission, Vision and Values + Logo together. The version for a webpage might be separated into 3 parts to make it easier to show on a webpage.

Good luck and happy designing

```html
<!DOCTYPE html>
<html lang="en">
<head>
<meta charset="utf-8">
<title>Vision | Mission | Values</title>
<link href="https://fonts.googleapis.com/css2?family=Arimo:wght@400;700&family=Roboto+Condensed:wght@400;700&display=swap" rel="stylesheet">
<style>
  :root {
    --navy: #1e3f7a;
    --heading-blue: #2a5aa0;
    --sky: #33a3dc;
    --purple: #5b1f5e;
    --green: #57a845;
    --yellow: #e8b321;
    --red: #b5202e;
    --orange: #e07a24;
    --blue: #1d4f91;
    --frame: #c9c9c9;
    --ink: #1b1b1b;
    --paper: #ffffff;
    --tick: #c8202f;
  }
  * { box-sizing: border-box; margin: 0; padding: 0; }
  html, body { width: 1200px; height: 869px; overflow: hidden; background: var(--paper); }
  .canvas { position: relative; width: 1200px; height: 869px; font-family: "Arimo", Arial, sans-serif; color: var(--ink); }
  .frame {
    position: absolute; left: 55px; top: 48px; width: 1131px; height: 800px;
    border: 10px solid var(--frame);
    background: linear-gradient(180deg, #ffffff 0%, #ffffff 45%, #d8eefa 100%);
  }
  .brand {
    position: absolute; left: 122px; top: 116px; width: 222px;
    font-family: "Roboto Condensed", sans-serif; font-weight: 700; font-size: 27px; line-height: 34px;
    color: var(--navy); white-space: nowrap;
  }
  .brand-divider { position: absolute; left: 352px; top: 85px; width: 2px; height: 98px; background: #bbb; }
  .pillars { position: absolute; left: 377px; top: 80px; list-style: none; }
  .pillars li { display: flex; align-items: center; gap: 10px; height: 38px; font-family: "Roboto Condensed", sans-serif; font-weight: 700; font-size: 21px; color: var(--navy); }
  .pillars svg { width: 20px; height: 20px; flex: 0 0 20px; }
  .banner {
    position: absolute; left: 117px; top: 200px; width: 490px; height: 44px;
    background: var(--navy); color: #fff; text-align: center;
    font-family: "Roboto Condensed", sans-serif; font-weight: 700; font-size: 36px; line-height: 44px; letter-spacing: 0.5px;
  }
  .section-title { position: absolute; left: 120px; font-family: "Arimo", sans-serif; font-weight: 700; font-size: 20px; line-height: 24px; color: var(--heading-blue); }
  .copy { position: absolute; left: 120px; width: 487px; font-size: 15px; line-height: 23px; text-align: justify; }
  .values { list-style: none; }
  .value { position: absolute; display: flex; gap: 10px; }
  .value-num { flex: 0 0 33px; color: #fff; font-family: "Roboto Condensed", sans-serif; font-size: 38px; text-align: center; }
  .value-text { font-size: 14.8px; line-height: 23px; }
  .value-text b { font-weight: 700; }
  .bar { position: absolute; top: 804px; height: 19px; }
  .bar-dark { left: 65px; width: 477px; background: var(--navy); }
  .bar-light { left: 558px; width: 618px; background: var(--sky); }
  .wheel { position: absolute; left: 646px; top: 51px; width: 496px; height: 496px; }
  .wheel-label { font-family: "Roboto Condensed", sans-serif; font-weight: 700; font-size: 27px; fill: #fff; letter-spacing: 2px; }
  .wheel-core { font-family: "Roboto Condensed", sans-serif; fill: #fff; }
</style>
</head>
<body>
<div class="canvas">
  <div class="frame"></div>

  <div class="brand">Brightway Therapy</div>
  <div class="brand-divider"></div>
  <ul class="pillars">
    <li><svg viewBox="0 0 20 20"><circle cx="10" cy="10" r="8.5" fill="none" stroke="var(--tick)" stroke-width="2.2"/><path d="M5.5 10 L9 13.5 L15 6" fill="none" stroke="var(--tick)" stroke-width="2.6" stroke-linecap="round" stroke-linejoin="round"/></svg>ENABLING CLIENTS</li>
    <li><svg viewBox="0 0 20 20"><circle cx="10" cy="10" r="8.5" fill="none" stroke="var(--tick)" stroke-width="2.2"/><path d="M5.5 10 L9 13.5 L15 6" fill="none" stroke="var(--tick)" stroke-width="2.6" stroke-linecap="round" stroke-linejoin="round"/></svg>EMPOWERING FAMILIES</li>
    <li><svg viewBox="0 0 20 20"><circle cx="10" cy="10" r="8.5" fill="none" stroke="var(--tick)" stroke-width="2.2"/><path d="M5.5 10 L9 13.5 L15 6" fill="none" stroke="var(--tick)" stroke-width="2.6" stroke-linecap="round" stroke-linejoin="round"/></svg>EDUCATING COMMUNITES</li>
  </ul>

  <div class="banner">VISION | MISSION | VALUES</div>

  <h2 class="section-title" style="top:257px">Our Vision:</h2>
  <p class="copy" style="top:286px">Individuals of all abilities will have the opportunity to achieve their therapy goals by accessing gold standard services, so they may confidently participate in the wider community where they will be understood, supported and embraced for their individuality.</p>

  <h2 class="section-title" style="top:388px">Our Mission:</h2>
  <p class="copy" style="top:418px">At Brightway Therapy we strive to ensure our clients and families have access to high quality, evidence-based intervention from a passionate and professional teams to improve and develop individual functional skills that contribute to successful participation in the community.</p>

  <h2 class="section-title" style="top:546px; font-size:18px">Our 6 Core Values:</h2>

  <ul class="values">
    <li class="value" style="left:91px; top:576px"><span class="value-num" style="background:var(--purple); height:67px; line-height:67px">1</span><p class="value-text" style="width:478px"><b>Quality</b> - We strive for excellence through evidence based practice, self-reflection, feedback and a continuous commitment to improvement and discovery both professionally and personally.</p></li>
    <li class="value" style="left:91px; top:659px"><span class="value-num" style="background:var(--green); height:67px; line-height:67px">2</span><p class="value-text" style="width:478px"><b>Integrity</b> - We care for and respect the needs and well-being of our families, our team and ourselves. We encourage openness, trust and honest communication at all times.</p></li>
    <li class="value" style="left:91px; top:739px"><span class="value-num" style="background:var(--yellow); height:42px; line-height:42px">3</span><p class="value-text" style="width:478px"><b>Diversity</b> - We embed diversity by recognising, respecting and appreciating differences in our families and our team.</p></li>
    <li class="value" style="left:632px; top:576px"><span class="value-num" style="background:var(--red); height:67px; line-height:67px">4</span><p class="value-text" style="width:445px"><b>Flexibility</b> - We are flexible in our problem solving and offer options and solutions for our families and team wherever we reasonably can.</p></li>
    <li class="value" style="left:632px; top:662px"><span class="value-num" style="background:var(--orange); height:44px; line-height:44px">5</span><p class="value-text" style="width:480px"><b>Positivity</b> - We lead ourselves, above the line, choosing to adopt a positive, accountable and solution-focused mindset.</p></li>
    <li class="value" style="left:632px; top:725px"><span class="value-num" style="background:var(--navy); height:67px; line-height:67px">6</span><p class="value-text" style="width:480px"><b>Creativity</b> - We are innovative and collaborative, constantly working towards new and improved ways to support our clients, families and our team.</p></li>
  </ul>

  <div class="bar bar-dark"></div>
  <div class="bar bar-light"></div>

  <svg class="wheel" viewBox="-248 -248 496 496" aria-label="Core values wheel">
    <defs>
      <path id="ring-path" d="M -222 0 A 222 222 0 1 1 222 0 A 222 222 0 1 1 -222 0"/>
      <path id="band" d="M -123 -213.04 A 246 246 0 0 1 123 -213.04 L 99 -171.47 A 198 198 0 0 0 -99 -171.47 Z"/>
      <path id="slice" d="M -95 -164.54 A 190 190 0 0 1 95 -164.54 L 36 -62.35 A 72 72 0 0 0 -36 -62.35 Z"/>
    </defs>
    <g stroke="#fff" stroke-width="5">
      <use href="#band" fill="var(--purple)"/>
      <use href="#band" fill="var(--green)" transform="rotate(60)"/>
      <use href="#band" fill="var(--yellow)" transform="rotate(120)"/>
      <use href="#band" fill="var(--red)" transform="rotate(180)"/>
      <use href="#band" fill="var(--orange)" transform="rotate(240)"/>
      <use href="#band" fill="var(--blue)" transform="rotate(300)"/>
    </g>
    <g stroke="#fff" stroke-width="5">
      <use href="#slice" fill="#6a2a6e" role="img" aria-label="Quality icon: award rosette"/>
      <use href="#slice" fill="#4d9a3c" transform="rotate(60)" role="img" aria-label="Integrity icon: handshake"/>
      <use href="#slice" fill="#dba51a" transform="rotate(120)" role="img" aria-label="Diversity icon: assorted shapes"/>
      <use href="#slice" fill="#a81d2a" transform="rotate(180)" role="img" aria-label="Flexibility icon: figure with arrows"/>
      <use href="#slice" fill="#d36f1e" transform="rotate(240)" role="img" aria-label="Positivity icon: thumbs up"/>
      <use href="#slice" fill="#1a4788" transform="rotate(300)" role="img" aria-label="Creativity icon: puzzle piece"/>
    </g>
    <text class="wheel-label" dominant-baseline="central" text-anchor="middle">
      <textPath href="#ring-path" startOffset="25%">QUALITY</textPath>
      <textPath href="#ring-path" startOffset="41.67%">INTEGRITY</textPath>
      <textPath href="#ring-path" startOffset="58.33%">DIVERSITY</textPath>
      <textPath href="#ring-path" startOffset="75%">FLEXIBILITY</textPath>
      <textPath href="#ring-path" startOffset="91.67%">POSITIVITY</textPath>
      <textPath href="#ring-path" startOffset="8.33%">CREATIVITY</textPath>
    </text>
    <circle r="66" fill="var(--sky)" stroke="#fff" stroke-width="6"/>
    <text class="wheel-core" y="-6" text-anchor="middle" font-size="34">CORE</text>
    <text class="wheel-core" y="26" text-anchor="middle" font-size="24">VALUES</text>
  </svg>
</div>
</body>
</html>
```